Company truck wrap design

We are The Drain Mending Works - We are looking to have the car wrapped, and need the expertise of a GD.

Below is the logo and photos of the truck.
1. We require an image to be created that offers a before and after of what we do - a story at a glance in essence

2. These images MUST be clean and pop! NO BACKGROUND effects - eg see images attached - we do not want any background imagery simply the pipe.

3. The image attached displays in essence what we require...
Tree roots, broken pipe and then a pipe that has been fixed with our resign (note the green) However,  In place of the green we would like our logo "the swirl" to be placed in the crack of the pipe replacing the single colour green .  We believe this will show exactly what we do in a simple and non verbal way.

4. We would like the images to run along of the upper sides of the canopy - as big as possible but not overpowering in size.

5. The back of the canopy could potentially have the pipe running around the top also. We require the logo contact number and website to be included on all sides

6. The dual cab two doors each side - The doors to display the logo, phone number and the website.

We are open to any suggestions - however - we like clean lines, bold but not overwhelming.

It would  be good to include
(dot points) - the dot could be our logo!
blocked drains
CCTV Inspections
Pipe Relining
Pipe Coating

I have included the brand guide
We are moving on this quickly

The Car is a 2020 VOLKAN TRAVERSO DUAL CAB

We look forward to receiving your work!

Smiles
Marjorie

Target Market(s)

Domestic and Commercial buildings

Requirements
Must have
• logo
phone number
website

```html
<!DOCTYPE html>
<html lang="en">
<head>
<meta charset="utf-8">
<title>The Drain Mending Works – Dual Cab Wrap</title>
<link rel="stylesheet" href="https://fonts.googleapis.com/css2?family=Exo+2:wght@400&family=Montserrat:wght@600;700;800&family=Roboto:wght@400;500&display=swap">
<style>
  :root {
    --paper: #ffffff;
    --ink: #000000;
    --ink-soft: #0d0d0d;
    --teal: #3adcd1;
    --mint: #a8e8b8;
    --white: #ffffff;
    --trim: #9a9a9a;
    --soil: #8b6a4a;
    --rust: #a4582c;
    --resin: #3e9b4a;
  }
  html, body {
    margin: 0;
    width: 1200px;
    height: 1200px;
    overflow: hidden;
    background: var(--paper);
  }
  .wrap-sheet { display: block; width: 1200px; height: 1200px; }
  .panel { fill: var(--ink); }
  .panel-back { fill: var(--ink-soft); }
  .glass { fill: var(--paper); }
  .door-trim { fill: none; stroke: var(--trim); stroke-width: 1.5; }
  .stripe-teal { fill: none; stroke: var(--teal); stroke-width: 6; }
  .stripe-mint { fill: none; stroke: var(--mint); stroke-width: 7; }
  .accent-mint { fill: var(--mint); }
  .brand-dot { fill: var(--mint); }
  .brand-name { font-family: "Exo 2", sans-serif; font-weight: 400; fill: var(--white); }
  .brand-rule { stroke: var(--white); stroke-width: 1.2; }
  .tagline { font-family: "Roboto", sans-serif; font-weight: 400; fill: var(--white); letter-spacing: 0.5px; }
  .phone { font-family: "Montserrat", sans-serif; font-weight: 800; fill: var(--mint); letter-spacing: 1px; }
  .web { font-family: "Roboto", sans-serif; font-weight: 500; fill: var(--white); }
  .web-lead { fill: var(--mint); }
  .social-dot { fill: var(--white); }
  .service-line { font-family: "Montserrat", sans-serif; font-weight: 700; fill: var(--teal); }
  .frame { fill: none; stroke: var(--trim); stroke-width: 1.5; }
  .tab { fill: var(--teal); }
  .tab-label { font-family: "Montserrat", sans-serif; font-weight: 800; fill: var(--ink); font-size: 12px; letter-spacing: 0.5px; }
  .headline { font-family: "Montserrat", sans-serif; font-weight: 700; fill: var(--teal); font-size: 17px; }
  .hero-dot { fill: var(--mint); stroke: var(--white); stroke-width: 3; }
</style>
</head>
<body>
<svg class="wrap-sheet" viewBox="0 0 1920 1920" xmlns="http://www.w3.org/2000/svg">
  <defs>
    <linearGradient id="pipe-story" x1="0" x2="1" y1="0" y2="0">
      <stop offset="0" stop-color="var(--rust)"/>
      <stop offset="0.5" stop-color="var(--soil)"/>
      <stop offset="0.85" stop-color="var(--rust)"/>
      <stop offset="1" stop-color="var(--resin)"/>
    </linearGradient>

    <g id="vehicle-side">
      <rect class="panel" x="219" y="368" width="564" height="316"/>
      <path class="panel" d="M217,696 L514,696 L465,773 L217,773 Z"/>
      <path class="accent-mint" d="M1410,529 L1690,570 Q1716,580 1721,604 L1705,603 Q1696,585 1680,580 Z"/>
      <path class="accent-mint" d="M1645,598 Q1660,640 1722,645 L1729,674 Q1662,652 1645,598 Z"/>
      <path class="panel" d="M806,465 Q815,418 850,416 L1145,416 Q1190,418 1235,440 L1415,532 L1688,575 Q1705,585 1705,602 L1645,596 Q1640,612 1655,630 Q1690,665 1755,685 L1757,712 L1744,725 Q1742,770 1700,775 L1655,780 Q1655,720 1610,680 Q1570,640 1528,640 Q1480,640 1445,665 Q1405,700 1395,782 L834,777 Q805,745 805,680 Z"/>
      <path class="glass" d="M860,436 L1048,436 L1047,545 L930,541 Q858,535 856,505 Z"/>
      <path class="glass" d="M1085,436 L1140,437 Q1200,440 1260,475 L1335,522 Q1345,545 1310,549 L1100,546 Z"/>
      <path class="door-trim" d="M850,428 L1230,432 Q1300,470 1352,528 L1360,735 Q1360,760 1335,760 L862,760 Q835,758 835,690 L835,450 Q836,430 850,428 Z"/>
      <line class="door-trim" x1="1069" y1="426" x2="1069" y2="760"/>
      <path class="stripe-mint" d="M219,571 L720,567 Q750,567 775,585 L800,600 L905,670 Q925,690 945,690 L1160,690"/>
      <path class="stripe-mint" d="M1275,693 L1405,690 Q1430,688 1455,668"/>
      <path class="stripe-teal" d="M219,546 L465,546 Q490,546 520,572 Q545,600 575,602 L900,602 Q930,602 950,618 L1155,778"/>
    </g>
  </defs>

  <!-- Driver side -->
  <use href="#vehicle-side"/>
  <g class="canopy-brand">
    <circle class="brand-dot" cx="415" cy="460" r="70"/>
    <text class="brand-name" font-size="34"><tspan x="504" y="420">THE DRAIN</tspan><tspan x="504" y="455">MENDING</tspan><tspan x="504" y="490">WORKS</tspan></text>
    <line class="brand-rule" x1="506" y1="500" x2="652" y2="500"/>
    <text class="tagline" x="506" y="521" font-size="13">NO DIG PIPE REPAIRS</text>
    <text class="phone" x="231" y="608" font-size="29">0400 555 218</text>
    <text class="web" x="231" y="627" font-size="18"><tspan class="web-lead">drain</tspan>mendingworks.com.au</text>
    <circle class="social-dot" cx="394" cy="638" r="5"/>
    <circle class="social-dot" cx="413" cy="638" r="5"/>
    <circle class="social-dot" cx="431" cy="638" r="5"/>
  </g>
  <g class="door-brand">
    <circle class="brand-dot" cx="1214" cy="618" r="42"/>
    <text class="brand-name" font-size="19"><tspan x="1171" y="681">THE DRAIN</tspan><tspan x="1171" y="700">MENDING</tspan><tspan x="1171" y="719">WORKS</tspan></text>
    <line class="brand-rule" x1="1172" y1="724" x2="1252" y2="724"/>
    <text class="tagline" x="1172" y="735" font-size="7">NO DIG PIPE REPAIRS</text>
    <text class="service-line" font-size="11"><tspan x="855" y="707">Advanced</tspan><tspan x="855" y="721">Trenchless</tspan><tspan x="855" y="735">Pipe Repair</tspan><tspan x="855" y="749">Professionals</tspan></text>
  </g>

  <!-- Passenger side -->
  <use href="#vehicle-side" transform="translate(1975,470) scale(-1,1)"/>
  <g class="canopy-brand">
    <circle class="brand-dot" cx="1382" cy="930" r="70"/>
    <text class="brand-name" font-size="34"><tspan x="1471" y="889">THE DRAIN</tspan><tspan x="1471" y="924">MENDING</tspan><tspan x="1471" y="959">WORKS</tspan></text>
    <line class="brand-rule" x1="1473" y1="970" x2="1620" y2="970"/>
    <text class="tagline" x="1473" y="991" font-size="13">NO DIG PIPE REPAIRS</text>
    <text class="phone" x="1740" y="1078" font-size="29" text-anchor="end">0400 555 218</text>
    <text class="web" x="1740" y="1097" font-size="18" text-anchor="end"><tspan class="web-lead">drain</tspan>mendingworks.com.au</text>
    <circle class="social-dot" cx="1696" cy="1107" r="5"/>
    <circle class="social-dot" cx="1714" cy="1107" r="5"/>
    <circle class="social-dot" cx="1733" cy="1107" r="5"/>
  </g>
  <g class="door-brand">
    <circle class="brand-dot" cx="760" cy="1088" r="42"/>
    <text class="brand-name" font-size="19"><tspan x="717" y="1150">THE DRAIN</tspan><tspan x="717" y="1169">MENDING</tspan><tspan x="717" y="1188">WORKS</tspan></text>
    <line class="brand-rule" x1="718" y1="1193" x2="798" y2="1193"/>
    <text class="tagline" x="718" y="1204" font-size="7">NO DIG PIPE REPAIRS</text>
    <text class="service-line" font-size="11" text-anchor="end"><tspan x="1113" y="1176">Advanced</tspan><tspan x="1113" y="1190">Trenchless</tspan><tspan x="1113" y="1204">Pipe Repair</tspan><tspan x="1113" y="1218">Professionals</tspan></text>
  </g>

  <!-- Canopy rear -->
  <g class="canopy-rear">
    <path class="panel-back" d="M860,1352 L1310,1352 L1352,1500 L1352,1665 L818,1665 L818,1500 Z"/>
    <path class="stripe-teal" d="M818,1529 L830,1529 Q840,1532 845,1547 L878,1665"/>
    <path class="stripe-mint" d="M818,1553 L828,1553 Q835,1556 838,1566 L866,1665"/>
    <path class="stripe-teal" d="M1352,1529 L1340,1529 Q1330,1532 1325,1547 L1292,1665"/>
    <path class="stripe-mint" d="M1352,1553 L1342,1553 Q1335,1556 1332,1566 L1304,1665"/>
    <rect class="frame" x="879" y="1372" width="411" height="280"/>
    <text class="headline" x="1082" y="1391" text-anchor="middle">Advanced Trenchless Pipe Repair Professionals</text>
    <rect x="879" y="1425" width="409" height="102" fill="url(#pipe-story)" role="img" aria-label="Before and after: cracked clay pipe invaded by tree roots, then the same pipe sealed with resin lining"/>
    <line x1="879" y1="1527" x2="1288" y2="1527" stroke="var(--teal)" stroke-width="3"/>
    <path class="tab" d="M879,1408 L962,1408 L980,1425 L879,1425 Z"/>
    <text class="tab-label" x="883" y="1421">BEFORE</text>
    <path class="tab" d="M1288,1408 L1205,1408 L1187,1425 L1288,1425 Z"/>
    <text class="tab-label" x="1284" y="1421" text-anchor="end">AFTER</text>
    <circle class="hero-dot" cx="1085" cy="1484" r="82"/>
    <text class="brand-name" font-size="27"><tspan x="897" y="1558">THE DRAIN</tspan><tspan x="897" y="1585">MENDING</tspan><tspan x="897" y="1612">WORKS</tspan></text>
    <line class="brand-rule" x1="898" y1="1620" x2="1009" y2="1620"/>
    <text class="tagline" x="898" y="1636" font-size="10">NO DIG PIPE REPAIRS</text>
    <text class="phone" x="1282" y="1604" font-size="24" text-anchor="end">0400 555 218</text>
    <text class="web" x="1282" y="1622" font-size="16" text-anchor="end"><tspan class="web-lead">drain</tspan>mendingworks.com.au</text>
    <circle class="social-dot" cx="1246" cy="1634" r="4.5"/>
    <circle class="social-dot" cx="1261" cy="1634" r="4.5"/>
    <circle class="social-dot" cx="1276" cy="1634" r="4.5"/>
  </g>
</svg>
</body>
</html>
```